Bright Oak Consultant Services

I'm looking to create a flyer for my business to provide a consultant service. I will be providing the following below
Launch Your Business Today for only $150
(state fee not included)
Business Formation includes:
*Limited liability Corporation (LLC)
*Hale and Penwick Number
*FEIN
*Operation Agreement for partnership LLCs (For 2 or more member(s)
*Commercial Activity license (If needed for your Business )
*Same -day turnaround service with documents
Schedule your Appointment today
Call or text:413-902-6175
Email:MorvellCapitalCircle@quillpost.net
Target Market(s)
I want the flyer to attract people who wants to start a business but doesn’t know where to start. I want the flyer to stand out form the other consultant businesses.
Industry/Entity Type
Consultant
Requirements
Must have
- The State fee not included should be in small print
Highlight the price or service
Highlight the phrase "launch you business today"
Nice to have
- Different samples of colors, a variety
Should not have
- should not be all one color

```html
<!DOCTYPE html>
<html lang="en">
<head>
<meta charset="utf-8">
<title>Bright Oak Consultant Services – Business Formation Flyer</title>
<link rel="stylesheet" href="https://fonts.googleapis.com/css2?family=Tinos:wght@400;700&family=Roboto+Condensed:wght@700&family=Open+Sans:wght@600&display=swap">
<style>
  :root {
    --page-bg: #5b5b5b;
    --paper: #ffffff;
    --ink: #0b0b0b;
    --brand-red: #e4334a;
    --price-red: #ef3340;
    --brand-orange: #e8651c;
    --frame-orange: #ec6a1f;
    --check-blue: #2a5aa8;
    --soft-peach: #f9d3b6;
    --divider: #c9c9c9;
    --light-text: #ffffff;
  }
  html, body {
    margin: 0;
    width: 900px;
    height: 1200px;
    overflow: hidden;
    background: var(--page-bg);
  }
  .flyer {
    position: absolute;
    left: 38px;
    top: 12px;
    width: 572px;
    height: 817px;
    background: var(--paper);
    transform: scale(1.44);
    transform-origin: top left;
    overflow: hidden;
    font-family: "Tinos", "Times New Roman", serif;
  }
  .contact-bar {
    position: absolute;
    left: 0; top: 40px;
    width: 100%; height: 30px;
    background: var(--brand-red);
  }
  .contact-email {
    position: absolute;
    right: 22px; top: 8px;
    display: flex; align-items: center; gap: 6px;
    font-family: "Open Sans", Arial, sans-serif;
    font-weight: 600;
    font-size: 8.6px;
    color: var(--light-text);
    letter-spacing: 0.1px;
  }
  .hero {
    position: absolute;
    left: 0; top: 70px;
    width: 100%; height: 302px;
    background: var(--ink);
  }
  .hero-visual {
    position: absolute;
    left: 296px; top: 0;
    width: 276px; height: 302px;
    background: radial-gradient(ellipse at 55% 48%, #6a6a6a 0%, #3a3a3a 35%, #141414 72%, #0b0b0b 100%);
  }
  .headline-frame {
    position: absolute;
    left: 25px; top: 12px;
    width: 271px; height: 338px;
    box-sizing: border-box;
    border: 3px solid var(--frame-orange);
  }
  .headline {
    position: absolute;
    left: 25px; top: 98px;
    width: 271px;
    text-align: center;
    color: var(--light-text);
  }
  .headline .line-light { font-size: 35px; line-height: 40px; font-weight: 400; }
  .headline .line-accent { font-size: 40px; line-height: 42px; font-weight: 700; color: var(--brand-orange); }
  .headline .line-bold { font-size: 21px; line-height: 26px; font-weight: 700; margin-top: 2px; }
  .headline .line-price { font-size: 26px; line-height: 44px; }
  .headline .price {
    font-family: "Roboto Condensed", Arial, sans-serif;
    font-weight: 700;
    font-size: 40px;
    color: var(--price-red);
  }
  .headline .fine-print { font-size: 13px; font-weight: 700; line-height: 18px; margin-top: 10px; }
  .includes-title {
    position: absolute;
    left: 0; top: 380px;
    width: 100%; height: 54px;
    background: var(--brand-red);
    display: flex; align-items: center; justify-content: center;
    font-size: 25.5px; font-weight: 700;
    color: var(--light-text);
    letter-spacing: 0.2px;
  }
  .includes-title .dark { color: var(--ink); margin-left: 7px; }
  .includes-panel {
    position: absolute;
    left: 0; top: 434px;
    width: 100%; height: 150px;
    background: linear-gradient(100deg, #f4f4f4 0%, #e2e2e2 30%, #f6f6f6 55%, #e8e8e8 80%, #f7f7f7 100%);
  }
  .panel-divider {
    position: absolute;
    left: 284px; top: 12px;
    width: 1px; height: 128px;
    background: var(--divider);
  }
  .item {
    position: absolute;
    display: flex; align-items: flex-start; gap: 14px;
    font-size: 16px; line-height: 20px;
    color: var(--ink);
  }
  .item svg { flex: none; }
  .item-llc { left: 44px; top: 30px; }
  .item-number { left: 44px; top: 90px; }
  .item-fein { left: 300px; top: 18px; }
  .item-agreement { left: 300px; top: 68px; line-height: 21px; }
  .item-agreement .text { margin-top: 3px; }
  .item .text { margin-top: 3px; }
  .extras-band {
    position: absolute;
    left: 0; top: 584px;
    width: 100%; height: 104px;
    background: var(--ink);
  }
  .extra {
    position: absolute;
    left: 42px;
    display: flex; align-items: center; gap: 12px;
    font-size: 16px;
    color: var(--light-text);
  }
  .extra-license { top: 12px; }
  .extra-turnaround { top: 50px; }
  .cta {
    position: absolute;
    left: 0; top: 700px;
    width: 100%; height: 117px;
    background: var(--brand-orange);
    text-align: center;
    color: var(--light-text);
  }
  .cta-lead { margin-top: 33px; font-size: 17px; line-height: 22px; color: var(--soft-peach); }
  .cta-phone { margin-top: 6px; font-size: 28px; line-height: 34px; }
  .cta-phone .number {
    font-family: "Roboto Condensed", Arial, sans-serif;
    font-weight: 700;
    font-size: 28px;
  }
</style>
</head>
<body>
  <div class="flyer">
    <div class="contact-bar">
      <div class="contact-email">
        <svg width="12" height="9" viewBox="0 0 12 9" aria-hidden="true">
          <rect x="0.6" y="0.6" width="10.8" height="7.8" fill="none" stroke="#fff" stroke-width="1"/>
          <path d="M0.8 0.9 L6 5 L11.2 0.9" fill="none" stroke="#fff" stroke-width="1"/>
        </svg>
        <span>MORVELLCAPITALCIRCLE@QUILLPOST.NET</span>
      </div>
    </div>

    <div class="hero">
      <div class="hero-visual" role="img" aria-label="Dark consulting concept image with business icons in hexagons"></div>
    </div>

    <div class="headline-frame"></div>
    <div class="headline">
      <div class="line-light">LAUNCH</div>
      <div class="line-light">YOUR</div>
      <div class="line-accent">BUSINESS</div>
      <div class="line-bold">TODAY FOR</div>
      <div class="line-price">ONLY <span class="price">$150</span></div>
      <div class="fine-print">(state fee not included)</div>
    </div>

    <div class="includes-title">BUSINESS FORMATION<span class="dark">INCLUDES</span></div>

    <div class="includes-panel" role="img" aria-label="Faint background photo of paperwork on a desk">
      <div class="panel-divider"></div>
      <div class="item item-llc">
        <svg width="30" height="30" viewBox="0 0 30 30" aria-hidden="true"><circle cx="14" cy="16" r="12.5" fill="#fff" stroke="#2a5aa8" stroke-width="1.6"/><path d="M8 15 L13 21 L25 6" fill="none" stroke="#e8651c" stroke-width="3" stroke-linecap="round" stroke-linejoin="round"/></svg>
        <div class="text">Limited liability<br>Corporation (LLC)</div>
      </div>
      <div class="item item-number">
        <svg width="30" height="30" viewBox="0 0 30 30" aria-hidden="true"><circle cx="14" cy="16" r="12.5" fill="#fff" stroke="#2a5aa8" stroke-width="1.6"/><path d="M8 15 L13 21 L25 6" fill="none" stroke="#e8651c" stroke-width="3" stroke-linecap="round" stroke-linejoin="round"/></svg>
        <div class="text">Hale and Penwick<br>Number</div>
      </div>
      <div class="item item-fein">
        <svg width="30" height="30" viewBox="0 0 30 30" aria-hidden="true"><circle cx="14" cy="16" r="12.5" fill="#fff" stroke="#2a5aa8" stroke-width="1.6"/><path d="M8 15 L13 21 L25 6" fill="none" stroke="#e8651c" stroke-width="3" stroke-linecap="round" stroke-linejoin="round"/></svg>
        <div class="text">FEIN</div>
      </div>
      <div class="item item-agreement">
        <svg width="30" height="30" viewBox="0 0 30 30" aria-hidden="true"><circle cx="14" cy="16" r="12.5" fill="#fff" stroke="#2a5aa8" stroke-width="1.6"/><path d="M8 15 L13 21 L25 6" fill="none" stroke="#e8651c" stroke-width="3" stroke-linecap="round" stroke-linejoin="round"/></svg>
        <div class="text">Operation Agreement for<br>partnership LLCs (For 2<br>or more member(s)</div>
      </div>
    </div>

    <div class="extras-band">
      <div class="extra extra-license">
        <svg width="32" height="30" viewBox="0 0 32 30" aria-hidden="true"><circle cx="14" cy="16" r="12.5" fill="none" stroke="#fff" stroke-width="1.6"/><path d="M7 15 L13 22 L28 4" fill="none" stroke="#e4334a" stroke-width="3.2" stroke-linecap="round" stroke-linejoin="round"/></svg>
        <span>Commercial Activity license (If needed for your Business )</span>
      </div>
      <div class="extra extra-turnaround">
        <svg width="32" height="30" viewBox="0 0 32 30" aria-hidden="true"><circle cx="14" cy="16" r="12.5" fill="none" stroke="#fff" stroke-width="1.6"/><path d="M7 15 L13 22 L28 4" fill="none" stroke="#e4334a" stroke-width="3.2" stroke-linecap="round" stroke-linejoin="round"/></svg>
        <span>Same -day turnaround service with documents</span>
      </div>
    </div>

    <div class="cta">
      <div class="cta-lead">schedule your Appointment today</div>
      <div class="cta-phone">CALL OR TEXT:<span class="number">413-902-6175</span></div>
    </div>
  </div>
</body>
</html>
```